Brightwell Assist Public Benefit Corporation - Initial Website

We need to develop an initial website for Brightwell Assist PBC. We are a startup managed business services provider focused on small business owners, entrepreneurs and their employees. We are a public benefit corporation and our public mission is to help business owners, entrepreneurs and their employees overcome the challenges that hold them back from reaching personal and professional success.
Our primary service offerings are managed business services that allow us to support the day-to-day operations of the businesses we support. This ongoing support provides the necessary pre-requisite relationship so we can provide effective and timely support when their organizations are experiencing challenges and moments of crisis. In those moments, it is our opportunity to help them overcome those challenges and stay on track for business utopia.
Our services are provided on a contract basis for a fixed monthly fee. We want to build strong relationships that help our clients grow their businesses while taking away the stresses associated with the backend of the business operations.
Finally, our public benefit is that we provide crisis invention, critical incident support, and mental health services to business owners and their employees during challenging times in an effort to improve their overall quality of life.

Coding

Coded - Design and coding required

```html
<!DOCTYPE html>
<html lang="en">
<head>
<meta charset="utf-8">
<title>Brightwell Assist Public Benefit Corporation</title>
<link href="https://fonts.googleapis.com/css2?family=Catamaran:wght@700;800&family=Poppins:wght@400;500;600;700&display=swap" rel="stylesheet">
<style>
:root{
  --navy:#0b1a4f;
  --orange:#f47412;
  --orange-soft:#fde6d4;
  --ink:#1f1f1f;
  --text:#3a3a3a;
  --grey-bg:#f2f2f2;
  --arc:#d4d4d4;
  --white:#ffffff;
}
*{margin:0;padding:0;box-sizing:border-box}
html,body{width:1200px;height:4278px;overflow:hidden}
body{position:relative;background:var(--white);font-family:"Poppins",sans-serif;color:var(--text)}
.abs{position:absolute}
.heading{font-family:"Catamaran",sans-serif;font-weight:800;color:var(--navy);text-transform:uppercase;letter-spacing:.5px}
.section-title{position:absolute;left:0;width:1200px;text-align:center;font-size:50px;line-height:1}
.title-bar{position:absolute;left:567px;width:66px;height:4px;border-radius:2px;background:var(--orange)}
.btn{position:absolute;display:flex;align-items:center;justify-content:center;background:var(--orange);color:var(--white);font-weight:600;font-size:14px;border-radius:24px;text-transform:uppercase;letter-spacing:.2px}
.social{position:absolute;width:34px;height:34px;border-radius:50%;background:var(--white);box-shadow:0 3px 8px rgba(0,0,0,.15)}
.social.active{background:var(--orange)}

/* header */
.logo-name{font-size:36px;font-weight:500;color:var(--orange);line-height:1}
.logo-sub{font-size:15px;font-weight:500;color:var(--orange);letter-spacing:.3px}
.nav a{position:absolute;top:58px;font-size:13px;font-weight:600;color:var(--ink);text-decoration:none;letter-spacing:.2px}
.nav a.current{color:var(--orange);border-bottom:2px solid var(--orange);padding-bottom:2px}
.nav-contact{position:absolute;left:808px;top:46px;width:135px;height:40px;border-radius:20px;background:var(--orange-soft);color:var(--orange);font-size:13px;font-weight:600;display:flex;align-items:center;justify-content:center}

/* hero */
.hero-photo{position:absolute;left:0;top:130px;width:1200px;height:610px;background:linear-gradient(100deg,#c9bdb1 0%,#e9e3dc 35%,#e4e0dc 60%,#b8b5b2 85%,#8a8683 100%)}
.hero-title{position:absolute;left:0;top:328px;width:1200px;text-align:center;font-size:47px;line-height:62px}
.dots{position:absolute;top:688px;left:560px;display:flex;gap:11px}
.dots span{width:10px;height:10px;border-radius:50%;background:var(--white)}
.dots span.on{background:var(--orange)}

/* mission */
.lead{position:absolute;left:140px;width:920px;top:912px;text-align:center;font-size:17px;line-height:27.5px;color:var(--ink)}
.photo-circle{position:absolute;left:111px;top:1060px;width:446px;height:446px;border-radius:50%;background:radial-gradient(circle at 65% 35%,#d6dde0,#8c969c 55%,#3f474d 100%)}
.copy p{font-size:15.5px;line-height:27.5px;color:var(--text);margin-bottom:11px}

/* services */
.services{position:absolute;left:0;top:1610px;width:1200px;height:938px;background:var(--grey-bg)}
.service-item{position:absolute;top:1843px;width:200px;text-align:center}
.service-icon{width:88px;height:88px;margin:0 auto;border-radius:50%;background:var(--white);box-shadow:0 4px 12px rgba(0,0,0,.12);display:flex;align-items:center;justify-content:center}
.service-item.active .service-icon{background:var(--orange);border:5px solid var(--white)}
.service-label{margin-top:20px;font-size:16.5px;font-weight:600;line-height:27px;color:var(--ink);text-transform:uppercase}
.service-item.active .service-label{color:var(--navy);text-decoration:underline;text-underline-offset:4px}
.arrow{position:absolute;top:1908px}
.detail-photo{position:absolute;left:601px;top:2063px;width:486px;height:390px;border-radius:14px;border:5px solid var(--white);box-shadow:0 5px 18px rgba(0,0,0,.18);background:linear-gradient(135deg,#c4c9cc 0%,#a8a39d 45%,#8a6e57 75%,#6a5848 100%)}

/* benefits */
.benefits-photo{position:absolute;left:0;top:2548px;width:1200px;height:532px;background:linear-gradient(90deg,#dcdcda 0%,#c8c3bc 20%,#b7b2ad 38%,#d9d9d7 52%,#e5e7e7 62%,#e8eaea 100%)}
.benefit-circle{position:absolute;left:633px;top:2576px;width:458px;height:458px;border-radius:50%;background:var(--white);box-shadow:0 0 0 14px rgba(255,255,255,.35)}

/* blog */
.blog-img{position:absolute;top:3288px;width:309px;height:221px;border-radius:12px 12px 0 0}
.blog-card{position:absolute;top:3486px;width:283px;height:249px;background:var(--white);border-radius:10px;box-shadow:0 4px 16px rgba(0,0,0,.13);padding:22px 22px 0}
.blog-card.active{border-bottom:4px solid var(--orange)}
.date-pill{display:inline-flex;align-items:center;gap:6px;height:30px;padding:0 14px;border:1px solid var(--orange);border-radius:15px;font-size:11px;color:var(--ink)}
.blog-title{margin-top:12px;font-size:15px;font-weight:600;line-height:25px;color:var(--ink);text-transform:uppercase}
.blog-text{margin-top:7px;font-size:13px;line-height:23px;color:var(--text)}
.read-more{display:inline-block;margin-top:6px;font-size:12px;font-weight:600;color:var(--orange);text-decoration:underline;text-underline-offset:3px}

/* footer */
.footer-h{position:absolute;top:3966px;font-size:16px;font-weight:600;color:var(--white);text-transform:uppercase}
.quick li{list-style:none;position:absolute;left:395px;font-size:14px;color:var(--white);display:flex;align-items:center;gap:18px}
.contact-line{position:absolute;left:583px;color:var(--white);font-size:12px;line-height:20px}
.contact-line b{display:block;font-size:13px;font-weight:600}
.contact-icon{position:absolute;left:550px}
</style>
</head>
<body>

<!-- Header -->
<header>
  <div class="abs" style="left:111px;top:38px">
    <div class="logo-name">Brightwell Assist</div>
    <div class="logo-sub" style="margin-top:4px">PUBLIC BENEFIT CORPORATION</div>
  </div>
  <nav class="nav">
    <a class="current" style="left:424px">HOME</a>
    <a style="left:489px">ABOUT US</a>
    <a style="left:580px">OUR SERVICES</a>
    <a style="left:701px">RESOURCES</a>
  </nav>
  <div class="nav-contact">CONTACT US</div>
  <div class="social active" style="left:968px;top:49px" aria-label="Social link"></div>
  <div class="social" style="left:1010px;top:49px" aria-label="Social link"></div>
  <div class="social" style="left:1052px;top:49px" aria-label="Social link"></div>
</header>

<!-- Hero -->
<section>
  <div class="hero-photo" role="img" aria-label="Team working on laptops at an office desk with a coffee mug"></div>
  <svg class="abs" style="left:0;top:130px" width="1200" height="610" viewBox="0 0 1200 610">
    <path d="M0 435 Q600 715 1200 435 L1200 610 L0 610 Z" fill="#ffffff"/>
    <path d="M0 435 Q600 715 1200 435 L1200 452 Q600 748 0 452 Z" fill="#d4d4d4"/>
  </svg>
  <h1 class="heading hero-title">Brightwell Assist<br>Public Benefit Corporation</h1>
  <div class="btn" style="left:523px;top:473px;width:154px;height:46px">Get Started</div>
  <div class="dots"><span></span><span class="on"></span><span></span><span></span></div>
</section>

<!-- Mission -->
<section>
  <h2 class="heading section-title" style="top:830px">Our Mission</h2>
  <div class="title-bar" style="top:878px"></div>
  <p class="lead">We are a startup managed business services provider focused on small business owners, entrepreneurs and their employees. We are a public benefit corporation and our public mission is to help business owners, entrepreneurs and their employees overcome the challenges that hold them back from reaching personal and professional success.</p>
  <div class="photo-circle" role="img" aria-label="Hands typing on a laptop with a glowing rocket launch graphic"></div>
  <div class="copy abs" style="left:634px;top:1095px;width:456px">
    <p>Lorem ipsum dolor sit amet, consectetur adipiscing elit, sed do eiusmod tempor incididunt ut labore et dolore magna aliqua. Ut enim ad minim veniam, quis nostrud exercitation ullamco laboris nisi ut aliquip ex ea commodo consequat. Duis aute irure dolor in reprehenderit in voluptate velit esse cillum dolore eu fugiat nulla pariatur.</p>
    <p>Lorem ipsum dolor sit amet, consectetur adipiscing elit, sed do eiusmod tempor incididunt ut labore et dolore magna aliqua. Ut enim ad minim veniam, quis nostrud exercitation ullamco laboris nisi ut aliquipea.</p>
  </div>
  <div class="btn" style="left:636px;top:1413px;width:179px;height:46px">Learn About Us</div>
</section>

<!-- Services -->
<section>
  <div class="services"></div>
  <h2 class="heading section-title" style="top:1698px">Our Services</h2>
  <div class="title-bar" style="top:1746px"></div>
  <p class="abs" style="left:0;top:1776px;width:1200px;text-align:center;font-size:20px;color:var(--ink)">Our services are provided on a contract basis for a fixed monthly fee.</p>

  <svg class="arrow" style="left:46px" width="18" height="28" viewBox="0 0 18 28"><path d="M14 3 L4 14 L14 25" fill="none" stroke="#9a9a9a" stroke-width="3"/></svg>
  <svg class="arrow" style="left:1136px" width="18" height="28" viewBox="0 0 18 28"><path d="M4 3 L14 14 L4 25" fill="none" stroke="#0b1a4f" stroke-width="3"/></svg>

  <div class="service-item" style="left:89px">
    <div class="service-icon"><svg width="46" height="46" viewBox="0 0 46 46" fill="none" stroke="#f47412" stroke-width="2"><rect x="6" y="8" width="34" height="24" rx="2"/><path d="M13 26V20M20 26V15M27 26V18M34 26V12"/><path d="M23 32V40M15 40H31"/></svg></div>
    <div class="service-label">Lorem Ipsum Sed<br>Dolor</div>
  </div>
  <div class="service-item" style="left:295px">
    <div class="service-icon"><svg width="46" height="46" viewBox="0 0 46 46" fill="none" stroke="#f47412" stroke-width="2"><circle cx="23" cy="12" r="5"/><circle cx="10" cy="32" r="5"/><circle cx="36" cy="32" r="5"/><path d="M20 16L13 27M26 16L33 27M15 33H31"/></svg></div>
    <div class="service-label">Lorem Ipsum Sed<br>Dolor</div>
  </div>
  <div class="service-item" style="left:499px">
    <div class="service-icon"><svg width="46" height="46" viewBox="0 0 46 46" fill="none" stroke="#f47412" stroke-width="2"><circle cx="23" cy="23" r="14"/><path d="M23 13V23L30 28"/><path d="M8 10L13 13M38 10L33 13"/></svg></div>
    <div class="service-label">Lorem Ipsum Sed<br>Dolor</div>
  </div>
  <div class="service-item active" style="left:703px">
    <div class="service-icon"><svg width="44" height="44" viewBox="0 0 46 46" fill="none" stroke="#ffffff" stroke-width="2"><path d="M6 24L14 16L22 20L30 14L40 22"/><path d="M14 26L22 34L30 28L36 32"/><circle cx="23" cy="10" r="4"/></svg></div>
    <div class="service-label">Managed Business<br>Services</div>
  </div>
  <div class="service-item" style="left:909px">
    <div class="service-icon"><svg width="46" height="46" viewBox="0 0 46 46" fill="none" stroke="#f47412" stroke-width="2"><circle cx="23" cy="23" r="7"/><path d="M23 6V12M23 34V40M6 23H12M34 23H40M11 11L15 15M31 31L35 35M35 11L31 15M15 31L11 35"/></svg></div>
    <div class="service-label">Lorem Ipsum Sed<br>Dolor</div>
  </div>

  <h3 class="heading abs" style="left:111px;top:2064px;font-size:35px;line-height:42px">Managed Business<br>Services</h3>
  <div class="copy abs" style="left:111px;top:2165px;width:428px">
    <p>Lorem ipsum dolor sit amet, consectetur adipiscing elit, sed do eiusmod tempor incididunt ut labore et dolore magna aliqua. Ut enim ad minim veniam, quis nostrud cillum dolore fugiat nulla pariatur.</p>
    <p>Lorem ipsum dolor sit amet, consectetur adipiscing elit, sed do eiusmod tempor incididunt ut labore et dolore tempor magna aliqua.</p>
  </div>
  <div class="btn" style="left:113px;top:2394px;width:146px;height:46px">Learn More</div>
  <div class="detail-photo" role="img" aria-label="Smiling business consultant with arms crossed in a brick-walled office with a team meeting behind"></div>
</section>

<!-- Benefits -->
<section>
  <div class="benefits-photo" role="img" aria-label="Group of professionals in a circle of chairs having a support discussion in a bright room"></div>
  <div class="benefit-circle"></div>
  <h2 class="heading abs" style="left:633px;top:2684px;width:458px;text-align:center;font-size:42px;line-height:1">Our Benefits</h2>
  <div class="abs" style="left:829px;top:2726px;width:66px;height:4px;border-radius:2px;background:var(--orange)"></div>
  <p class="abs" style="left:672px;top:2758px;width:380px;text-align:center;font-size:14.5px;line-height:27.5px;color:var(--ink)">Our public benefit is that we provide crisis invention, critical incident support, and mental health services to business owners and their employees during challenging times in an effort to improve their overall quality of life.</p>
  <div class="btn" style="left:785px;top:2922px;width:154px;height:46px">Contact Us</div>
</section>

<!-- Blog -->
<section>
  <h2 class="heading section-title" style="top:3188px">Latest Blog</h2>
  <div class="title-bar" style="top:3236px"></div>

  <div class="blog-img" style="left:111px;background:linear-gradient(160deg,#dfe4e2,#b7b3aa 55%,#7d7469)" role="img" aria-label="Presenter speaking to a seated business team"></div>
  <div class="blog-img" style="left:445px;background:radial-gradient(circle at 50% 45%,#f2a24a 0,#6b5a43 18%,#27343a 55%,#1c2529 100%)" role="img" aria-label="Laptop with a glowing light bulb idea on a dark desk"></div>
  <div class="blog-img" style="left:780px;background:linear-gradient(120deg,#e9ecec,#b8c0c6 45%,#5f6e7c 80%,#3c4652)" role="img" aria-label="Colleagues planning together at a whiteboard"></div>

  <article class="blog-card" style="left:124px">
    <span class="date-pill"><svg width="11" height="11" viewBox="0 0 12 12" fill="none" stroke="#f47412" stroke-width="1.4"><rect x="1" y="2" width="10" height="9" rx="1"/><path d="M1 5H11M4 1V3M8 1V3"/></svg>01 NOV 2024</span>
    <h3 class="blog-title">Lorem Ipsum Dolor Sit<br>Consectetur</h3>
    <p class="blog-text">Lorem ipsum dolor sit amet, conse adipiscing elit, sed do eiusmod tempor incididunt laborea.</p>
    <span class="read-more">READ MORE</span>
  </article>
  <article class="blog-card active" style="left:458px">
    <span class="date-pill"><svg width="11" height="11" viewBox="0 0 12 12" fill="none" stroke="#f47412" stroke-width="1.4"><rect x="1" y="2" width="10" height="9" rx="1"/><path d="M1 5H11M4 1V3M8 1V3"/></svg>01 NOV 2024</span>
    <h3 class="blog-title">Lorem Ipsum Dolor Sit<br>Consectetur</h3>
    <p class="blog-text">Lorem ipsum dolor sit amet, conse adipiscing elit, sed do eiusmod tempor incididunt laborea.</p>
    <span class="read-more">READ MORE</span>
  </article>
  <article class="blog-card" style="left:793px">
    <span class="date-pill"><svg width="11" height="11" viewBox="0 0 12 12" fill="none" stroke="#f47412" stroke-width="1.4"><rect x="1" y="2" width="10" height="9" rx="1"/><path d="M1 5H11M4 1V3M8 1V3"/></svg>01 NOV 2024</span>
    <h3 class="blog-title">Lorem Ipsum Dolor Sit<br>Consectetur</h3>
    <p class="blog-text">Lorem ipsum dolor sit amet, conse adipiscing elit, sed do eiusmod tempor incididunt laborea.</p>
    <span class="read-more">READ MORE</span>
  </article>
</section>

<!-- Footer -->
<footer>
  <svg class="abs" style="left:0;top:3840px" width="1200" height="438" viewBox="0 0 1200 438">
    <path d="M0 145 Q600 -121 1200 145 L1200 438 L0 438 Z" fill="#d9d9d9"/>
    <path d="M0 172 Q600 -82 1200 172 L1200 438 L0 438 Z" fill="#0b1a4f"/>
  </svg>

  <div class="abs" style="left:111px;top:4030px">
    <div class="logo-name" style="color:var(--white);font-size:34px">Brightwell Assist</div>
    <div class="logo-sub" style="color:var(--white);margin-top:4px">PUBLIC BENEFIT CORPORATION</div>
  </div>
  <div class="social active" style="left:177px;top:4105px;box-shadow:none" aria-label="Social link"></div>
  <div class="social" style="left:217px;top:4105px;background:transparent;border:1.5px solid #fff;box-shadow:none" aria-label="Social link"></div>
  <div class="social" style="left:257px;top:4105px;background:transparent;border:1.5px solid #fff;box-shadow:none" aria-label="Social link"></div>

  <div class="footer-h" style="left:395px">Quick Links</div>
  <ul class="quick">
    <li style="top:4013px"><svg width="13" height="13" viewBox="0 0 14 14"><circle cx="7" cy="7" r="7" fill="#f47412"/><path d="M5 4L8.5 7L5 10" stroke="#fff" stroke-width="1.6" fill="none"/></svg>Home</li>
    <li style="top:4052px"><svg width="13" height="13" viewBox="0 0 14 14"><circle cx="7" cy="7" r="7" fill="#f47412"/><path d="M5 4L8.5 7L5 10" stroke="#fff" stroke-width="1.6" fill="none"/></svg>About Us</li>
    <li style="top:4090px"><svg width="13" height="13" viewBox="0 0 14 14"><circle cx="7" cy="7" r="7" fill="#f47412"/><path d="M5 4L8.5 7L5 10" stroke="#fff" stroke-width="1.6" fill="none"/></svg>Our Services</li>
    <li style="top:4129px"><svg width="13" height="13" viewBox="0 0 14 14"><circle cx="7" cy="7" r="7" fill="#f47412"/><path d="M5 4L8.5 7L5 10" stroke="#fff" stroke-width="1.6" fill="none"/></svg>Resources</li>
    <li style="top:4167px"><svg width="13" height="13" viewBox="0 0 14 14"><circle cx="7" cy="7" r="7" fill="#f47412"/><path d="M5 4L8.5 7L5 10" stroke="#fff" stroke-width="1.6" fill="none"/></svg>Contact Us</li>
  </ul>

  <div class="footer-h" style="left:549px">Contact Info</div>
  <svg class="contact-icon" style="top:4016px" width="11" height="15" viewBox="0 0 12 16"><path d="M6 0C2.7 0 0 2.6 0 5.8 0 10 6 16 6 16S12 10 12 5.8C12 2.6 9.3 0 6 0Z" fill="#f47412"/><circle cx="6" cy="6" r="2.2" fill="#0b1a4f"/></svg>
  <div class="contact-line" style="top:4012px"><b>ADDRESS:</b>465, Lorum Ipsum Dolore,<br>United States</div>
  <svg class="contact-icon" style="top:4094px" width="13" height="13" viewBox="0 0 14 14"><path d="M3 1L5.5 3.5 4 5.5C5 7.5 6.5 9 8.5 10L10.5 8.5 13 11 11.5 13C6 13 1 8 1 2.5Z" fill="#f47412"/></svg>
  <div class="contact-line" style="top:4090px"><b>PHONE:</b>+1 (888) 888 8888</div>
  <svg class="contact-icon" style="top:4152px" width="14" height="11" viewBox="0 0 14 11"><rect width="14" height="11" rx="1.5" fill="#f47412"/><path d="M1 1.5L7 6 13 1.5" stroke="#0b1a4f" stroke-width="1.3" fill="none"/></svg>
  <div class="contact-line" style="top:4148px"><b>EMAIL:</b>info@brightwellassistpbc.com</div>

  <div class="footer-h" style="left:780px">Newsletter Signup</div>
  <div class="abs" style="left:780px;top:4019px;width:308px;height:46px;border-radius:23px;background:var(--white);display:flex;align-items:center;justify-content:space-between;padding:0 4px 0 17px">
    <span style="font-size:13px;color:#6a6a6a">Email Address</span>
    <span style="width:102px;height:38px;border-radius:19px;background:var(--orange);color:#fff;font-size:13px;font-weight:600;display:flex;align-items:center;justify-content:center">SIGN UP</span>
  </div>

  <div class="abs" style="left:111px;top:4218px;width:978px;height:1px;background:rgba(255,255,255,.25)"></div>
  <p class="abs" style="left:0;top:4236px;width:1200px;text-align:center;font-size:13px;color:var(--white)">© 2024 BRIGHTWELL ASSIST PBC &nbsp;-&nbsp; All Rights Reserved</p>
</footer>

</body>
</html>
```